Need a flyer overhaul and minor changes

flyer is 5.5" x 8.5" we need to change the $250.00 to $325.00, update our company logo on the brochure, and also have an area where we can have the store address (318 W Harlan Ave, Del Rio, TX 78840 - (830) 642-9158). I've attached a our current brochure and our updated logo and we just want to make look better and updated.

Industry/Entity Type

Lending and Finance

Requirements
Nice to have
• updated layout and pictures

```html
<!DOCTYPE html>
<html lang="en">
<head>
<meta charset="utf-8">
<title>Title Loan Flyer</title>
<link href="https://fonts.googleapis.com/css2?family=Lora:wght@600;700&display=swap" rel="stylesheet">
<style>
  :root {
    --red: #c9161f;
    --green: #0b5e2e;
    --paper: #efefef;
    --panel: #ffffff;
    --ink: #1d1d1d;
    --stage: #e4e4e4;
  }
  html, body { margin: 0; padding: 0; width: 1200px; height: 1200px; overflow: hidden; background: var(--stage); }
  body { font-family: "Lora", Georgia, serif; }
  .flyer { position: absolute; left: 250px; top: 59px; width: 700px; height: 1082px; overflow: hidden; background: var(--paper); box-shadow: 0 6px 24px rgba(0,0,0,.18); }
  .flyer-shapes { position: absolute; inset: 0; }
  .headline { position: absolute; left: 46px; top: 34px; margin: 0; color: #fff; font-weight: 700; line-height: 1; transform: rotate(9deg); transform-origin: left top; }
  .headline .lead { display: block; font-size: 54px; }
  .headline .main { display: block; font-size: 62px; letter-spacing: 1px; }
  .brand-badge { position: absolute; left: 540px; top: 185px; width: 150px; text-align: center; color: var(--green); font-weight: 700; font-size: 21px; line-height: 1.1; }
  .comparison-title { position: absolute; left: 40px; top: 232px; width: 340px; height: 40px; line-height: 40px; text-align: center; color: #fff; font-size: 19px; font-weight: 700; letter-spacing: .5px; }
  .comparison { position: absolute; left: 40px; top: 285px; width: 340px; display: grid; grid-template-columns: 1fr 1fr; text-align: center; color: var(--ink); }
  .comparison .col-head { font-size: 16px; font-weight: 700; color: var(--green); height: 44px; line-height: 44px; }
  .comparison .amount { font-size: 21px; font-weight: 700; height: 36px; line-height: 36px; }
  .pill { position: absolute; color: #fff; font-weight: 700; text-align: center; border-radius: 22px; }
  .pill-paid { left: 48px; top: 780px; width: 156px; height: 42px; line-height: 42px; background: var(--green); font-size: 20px; }
  .pill-owe { left: 218px; top: 780px; width: 156px; height: 42px; background: var(--red); display: flex; align-items: center; justify-content: center; gap: 8px; font-size: 22px; }
  .pill-owe small { font-size: 11px; line-height: 1; text-align: left; }
  .spanish { position: absolute; left: 438px; top: 860px; color: #fff; font-size: 18px; font-weight: 700; letter-spacing: .5px; }
  .call-now { position: absolute; left: 40px; top: 845px; color: #fff; font-size: 38px; font-weight: 700; }
  .phone { position: absolute; left: 320px; top: 900px; width: 380px; height: 66px; line-height: 66px; background: var(--red); color: #fff; font-size: 48px; font-weight: 700; border-radius: 34px 0 0 34px; padding-left: 24px; box-sizing: border-box; }
  .web { position: absolute; left: 30px; top: 985px; color: #fff; font-weight: 700; text-align: center; width: 290px; }
  .web .label { display: block; font-size: 17px; }
  .web .url { display: block; font-size: 18px; }
  .address { position: absolute; left: 356px; top: 1000px; color: #fff; font-weight: 700; font-size: 18px; line-height: 1.35; }
</style>
</head>
<body>
<div class="flyer">
  <svg class="flyer-shapes" viewBox="0 0 700 1082" width="700" height="1082" aria-hidden="true">
    <defs>
      <linearGradient id="photoTone" x1="0" y1="0" x2="1" y2="1">
        <stop offset="0" stop-color="#b9a596"/>
        <stop offset=".45" stop-color="#8c7a6f"/>
        <stop offset="1" stop-color="#3a3634"/>
      </linearGradient>
    </defs>
    <rect x="300" y="210" width="400" height="720" fill="url(#photoTone)" role="img" aria-label="Photo of a smiling woman holding a fan of hundred-dollar bills"/>
    <path d="M0 0 H700 V245 C520 262 300 230 0 120 Z" fill="var(--green)"/>
    <path d="M0 0 H700 V230 C520 248 300 214 0 106 Z" fill="var(--red)"/>
    <circle cx="620" cy="225" r="100" fill="#fff" stroke="var(--green)" stroke-width="7"/>
    <rect x="40" y="232" width="340" height="40" rx="14" fill="var(--green)"/>
    <rect x="40" y="262" width="340" height="548" rx="18" fill="var(--panel)"/>
    <line x1="210" y1="290" x2="210" y2="790" stroke="#dcdcdc" stroke-width="1.5"/>
    <path d="M0 790 C40 800 40 835 120 835 H380 C480 840 560 870 700 905 V1082 H0 Z" fill="var(--green)"/>
    <path d="M0 950 C140 920 270 960 340 1082 H0 Z" fill="var(--red)"/>
  </svg>

  <h1 class="headline"><span class="lead">Stuck in a</span><span class="main">TITLE LOAN?</span></h1>
  <div class="brand-badge">Ledgerline<br>Lending</div>

  <div class="comparison-title">$1,000 LOAN COMPARISON</div>
  <div class="comparison">
    <div class="col-head">LEDGERLINE</div><div class="col-head">TITLE LOAN</div>
    <div class="amount">$131.67</div><div class="amount">$325.00</div>
    <div class="amount">$131.67</div><div class="amount">$325.00</div>
    <div class="amount">$131.67</div><div class="amount">$325.00</div>
    <div class="amount">$131.67</div><div class="amount">$325.00</div>
    <div class="amount">$131.67</div><div class="amount">$325.00</div>
    <div class="amount">$131.67</div><div class="amount">$325.00</div>
    <div class="amount">$131.67</div><div class="amount">$325.00</div>
    <div class="amount">$131.67</div><div class="amount">$325.00</div>
    <div class="amount">$131.67</div><div class="amount">$325.00</div>
    <div class="amount">$131.67</div><div class="amount">$325.00</div>
    <div class="amount">$131.67</div><div class="amount">$325.00</div>
    <div class="amount">$131.67</div><div class="amount">$325.00</div>
  </div>
  <div class="pill pill-paid">PAID OFF</div>
  <div class="pill pill-owe"><small>STILL<br>OWE</small><span>$1,000</span></div>

  <div class="spanish">SE HABLA ESPAÑOL</div>
  <div class="call-now">CALL US NOW</div>
  <div class="phone">956-417-3860</div>
  <div class="web"><span class="label">VISIT US AT</span><span class="url">LEDGERLINELENDING.COM</span></div>
  <div class="address">318 W Harlan Ave, Del Rio,<br>TX 78840 - (830) 642-9158</div>
</div>
</body>
</html>
```